Redesign this Sydney Chocolatier Website

We are looking for a redesign of this websites home page and product pages.

https://marlowconfections.com.au/

Marlow Confections have been making handmade chocolates in Sydney Australia since 1932 they specialize in making hand made chocolates without additives, without palm oil and using all-natural ingredients.

We are looking to rebrand the company to reposition the brand in the high-quality chocolate gifts and hampers market as such they have launched products to tackle this market.

https://marlowconfections.com.au/hampers-2/

Some of the players in this market that we would like to compete with are

https://www.thegiftcrategallery.com.au/

https://www.brindlecocoa.com.au/

https://www.chocolate.vesperine.com/

The website is currently built on Kavo Woo-commerce and though it looks decent in our opinion the home page is a little busy and does not convey the quality of the brand.

We are looking for something cleaner that will perform great especially on mobiles.

Target Market(s)

Families and business owners 40+ affluent we specialise in luxury chocolates hampers and chocolate gifts the current look lacks the high end look.

Number of Pages Required

2 page

Font styles to use
Script

Requirements
Must have
• Good SEO Footer, easy to navigate, cleaner than the original design, presents well on mobile devices, plant of room for copy I have included a copy doc with the actual home page copy.
Nice to have
• Something more stylish and high end looking that will appeal to the target market. clean navigation and easy to use that again translates well to mobile, you can use divs and read mores to declutter the long SEO texts see suggested copy doc (you do not have to use all of this
Should not have
• Less cluttered more stylish design than the original website

```html
<!DOCTYPE html>
<html lang="en">
<head>
<meta charset="utf-8">
<title>Marlow Confections – Handmade Chocolates Since 1932</title>
<link href="https://fonts.googleapis.com/css2?family=Great+Vibes&family=Montserrat:wght@400;500&family=Playfair+Display:ital,wght@0,500;1,400&display=swap" rel="stylesheet">
<style>
:root{
  --gold:#b8976a;
  --gold-soft:#efe4d3;
  --ink:#222;
  --hero:#6a4a3e;
  --hero-dark:#3f2a23;
  --cream:#fdf0cc;
  --toffee:#8f5d22;
  --footer:#9a6a35;
  --navy:#2b2466;
  --white:#fff;
}
*{box-sizing:border-box;margin:0;padding:0}
html,body{width:1200px;height:3596px;overflow:hidden}
body{position:relative;background:var(--white);font-family:"Montserrat",sans-serif;color:var(--ink)}
.abs{position:absolute}
.script{font-family:"Great Vibes",cursive;font-weight:400}
.serif{font-family:"Playfair Display",serif}

/* header */
.site-header{left:0;top:0;width:1200px;height:84px}
.brand{left:117px;top:18px;color:var(--gold);font-size:26px;font-weight:500;letter-spacing:1px;display:flex;align-items:center;gap:8px}
.brand-dot{width:10px;height:10px;border:2px solid var(--gold);border-radius:50%}
.main-nav{right:117px;top:30px;display:flex;gap:26px;font-size:13px;align-items:center}
.main-nav span{display:flex;align-items:center;gap:10px}

/* hero */
.hero{left:0;top:84px;width:1200px;height:555px;background:radial-gradient(circle at 62% 50%,#8a675a 0%,var(--hero) 40%,var(--hero-dark) 100%)}
.hero-title{left:117px;top:190px;font-size:78px;color:var(--white)}
.hero-sub{left:117px;top:308px;font-size:23px;line-height:28px;color:var(--white);font-weight:500}
.btn{display:flex;align-items:center;justify-content:center;font-size:12px;letter-spacing:.5px;text-transform:uppercase}
.btn-light{background:var(--white);color:var(--ink)}
.hero-btn{left:119px;top:445px;width:207px;height:49px}

/* welcome */
.welcome-title{left:117px;top:686px;font-size:44px;color:var(--ink)}
.welcome-copy{left:119px;top:757px;width:650px;font-size:12px;line-height:32px;letter-spacing:-.1px}
.welcome-brand{left:830px;top:782px;width:160px;text-align:center;color:var(--gold);font-size:30px;font-weight:500}
.btn-outline{border:2px solid var(--gold);color:var(--ink)}
.welcome-btn{left:117px;top:927px;width:208px;height:51px;font-size:11px}

/* feature slider */
.feature-icon{left:486px;top:1006px;width:228px;height:228px;border-radius:50%;background:radial-gradient(circle,var(--gold-soft) 0%,#d9c4a4 100%)}
.arrow-gold{top:1200px}
.feature-title{left:0;top:1268px;width:1200px;text-align:center;font-size:32px;font-weight:500}
.feature-copy{left:255px;top:1329px;width:690px;text-align:center;font-size:16.5px;line-height:42px}

/* category tiles */
.tile{overflow:hidden}
.tile-media{position:absolute;inset:0}
.tile-heading{position:absolute;border:2px solid var(--white);color:var(--white);font-size:34px;padding:0 18px;height:44px;line-height:46px}
.tile-copy{position:absolute;color:var(--white);font-size:16.5px;line-height:32px}
.tile-btn{position:absolute;width:207px;height:50px;font-size:13px}
.tile-chocolates{left:117px;top:1529px;width:966px;height:395px}
.tile-gifts{left:117px;top:1928px;width:360px;height:343px}
.tile-corporate{left:481px;top:1928px;width:602px;height:343px}

/* promo grid */
.promo{width:483px;height:209px}
.promo-text{background:var(--cream);padding:14px 26px;font-size:16.5px;line-height:42px}
.btn-dark{background:var(--toffee);color:var(--white);font-size:13px}

/* testimonials */
.testi-title{left:0;top:2888px;width:1200px;text-align:center;font-size:26px;font-weight:500}
.testi-copy{left:240px;top:2944px;width:720px;text-align:center;font-size:16.5px;line-height:32px}
.stars{left:0;top:3100px;width:1200px;text-align:center;color:#f2d21a;font-size:18px;letter-spacing:1px}
.testi-rule{left:382px;top:3133px;width:436px;height:1px;background:#444}
.testi-name{left:0;top:3140px;width:1200px;text-align:center;font-style:italic;font-size:15px}
.testi-role{left:0;top:3163px;width:1200px;text-align:center;font-style:italic;font-size:11px}

/* footer */
.site-footer{left:0;top:3238px;width:1200px;height:358px;background:var(--footer);color:var(--white)}
.footer-head{font-size:23px;letter-spacing:.5px;font-weight:400}
.footer-list{font-size:13px;line-height:26.5px;list-style:none}
.newsletter-input{left:691px;top:100px;width:274px;height:48px;background:var(--white);color:#999;font-size:13px;padding:0 18px;display:flex;align-items:center}
.newsletter-btn{left:965px;top:100px;width:118px;height:48px;background:var(--navy);color:var(--white);font-size:11px}
.social{left:691px;top:222px;display:flex;gap:14px}
.social span{width:24px;height:24px;border-radius:50%;background:var(--white)}
.map-btn{left:117px;top:247px;width:223px;height:48px;font-size:10px}
.footer-rule{left:117px;top:307px;width:966px;height:1px;background:rgba(255,255,255,.8)}
.copyright{left:117px;top:324px;font-size:11.5px;font-variant:small-caps;letter-spacing:.3px}
</style>
</head>
<body>

<header class="abs site-header">
  <div class="abs brand"><span class="brand-dot"></span>Marlow</div>
  <nav class="abs main-nav">
    <span>CHOCOLATES <svg width="18" height="10" viewBox="0 0 18 10"><path d="M2 2l7 6 7-6" fill="none" stroke="var(--gold)" stroke-width="3"/></svg></span>
    <span>SPECIAL EVENTS <svg width="18" height="10" viewBox="0 0 18 10"><path d="M2 2l7 6 7-6" fill="none" stroke="var(--gold)" stroke-width="3"/></svg></span>
    <span>GIFTS &amp; HAMPERS <svg width="18" height="10" viewBox="0 0 18 10"><path d="M2 2l7 6 7-6" fill="none" stroke="var(--gold)" stroke-width="3"/></svg></span>
    <span>CONTACT</span>
    <span><svg width="22" height="20" viewBox="0 0 22 20"><path d="M1 2h4l3 11h11l2-8H7" fill="none" stroke="var(--gold)" stroke-width="2"/><circle cx="9" cy="17" r="2" fill="var(--gold)"/><circle cx="17" cy="17" r="2" fill="var(--gold)"/></svg>CART</span>
  </nav>
</header>

<section class="abs hero" role="img" aria-label="Swirling spiral of rich melted chocolate"></section>
<h1 class="abs hero-title script">Marlow chocolates</h1>
<p class="abs hero-sub">Delicious hand-crafted chocolates<br>made in Sydney since 1932</p>
<a class="abs btn btn-light hero-btn">Shop now</a>

<h2 class="abs welcome-title script">Welcome to Marlow</h2>
<p class="abs welcome-copy">Marlow Confections was founded by Samuel Marlow in 1932. Samuel had a passion for making handmade chocolate from his kitchen in Paddington. In time, he became a master at his craft and developed a loyal customer following. From his efforts, some of Australia’s most delicious fondants, hard centres, jellies and gingers coated with the finest chocolate were conceived. Samuel is no longer with us, but his passion for fine handmade chocolates and the original recipes on which the Marlow brand was built endure...</p>
<div class="abs welcome-brand">Marlow</div>
<a class="abs btn btn-outline welcome-btn">Leran more</a>

<svg class="abs arrow-gold" style="left:114px" width="28" height="44" viewBox="0 0 28 44"><path d="M22 4L6 22l16 18" fill="none" stroke="var(--gold)" stroke-width="6"/></svg>
<svg class="abs arrow-gold" style="left:1056px" width="28" height="44" viewBox="0 0 28 44"><path d="M6 4l16 18L6 40" fill="none" stroke="var(--gold)" stroke-width="6"/></svg>
<div class="abs feature-icon" role="img" aria-label="Gluten free emblem: crossed-out wheat sprig in a gold circle"></div>
<h3 class="abs feature-title serif">Gluten Free</h3>
<p class="abs feature-copy">In recent years, many customers began asking us to cater for chocolate lovers who are gluten intolerant ... And for a while, we were unfortunately unable to meet that request. We’re happy to say that’s changed! All the handmade chocolates sold on our website are gluten free!</p>

<article class="abs tile tile-chocolates">
  <div class="tile-media" role="img" aria-label="Box of assorted handmade chocolates on a dark marbled surface" style="background:linear-gradient(120deg,#1f2630 0%,#3a2b26 45%,#1c2a3a 75%,#40546a 100%)"></div>
  <h3 class="tile-heading script" style="left:46px;top:42px">Our Chocolates</h3>
  <p class="tile-copy" style="left:42px;top:114px;width:520px">Delicious chocolates in a great variety of flavours, handmade to perfection in our Sydney factory, and delivered to your door throughout Australia. Discover Marlow today!</p>
  <a class="tile-btn btn btn-light" style="left:733px;top:317px">View prodducts</a>
</article>

<article class="abs tile tile-gifts">
  <div class="tile-media" role="img" aria-label="Wrapped gift boxes and hampers" style="background:linear-gradient(135deg,#3a1e1a 0%,#6a2a22 40%,#2a4a40 75%,#5a3a28 100%)"></div>
  <h3 class="tile-heading script" style="left:44px;top:40px">Gifts &amp; Hampers</h3>
  <p class="tile-copy" style="left:44px;top:104px;width:280px">As with all our chocolates, our hampers are handmade with care from our Kingsgrove shop and hand-wrapped and styled to suit the occasion.</p>
  <a class="tile-btn btn btn-light" style="left:126px;top:265px">View prodducts</a>
</article>

<article class="abs tile tile-corporate">
  <div class="tile-media" role="img" aria-label="Hands holding a striped chocolate truffle above a dark background" style="background:linear-gradient(160deg,#2a1e1a 0%,#0e0a08 45%,#1a1210 80%,#3a2a20 100%)"></div>
  <h3 class="tile-heading script" style="left:44px;top:40px">Corporate &amp; personalized</h3>
  <p class="tile-copy" style="left:44px;top:104px;width:560px">Give a very special and memorable gift to partners, clients and prospects with branded packaging and personalised cards. Bring a box of delicious Marlow chocolates to your next meeting. You’ll be remembered for more than your just your work!</p>
  <a class="tile-btn btn btn-light" style="left:369px;top:265px">View prodducts</a>
</article>

<div class="abs promo promo-text" style="left:116px;top:2394px">
  <p style="width:420px">Enjoy our flavour packed handcrafted chocolates today with friends, clients and family. Any day is a good day for handmade chocolates from one of Australia’s oldest</p>
  <a class="abs btn btn-dark" style="left:258px;top:140px;width:207px;height:50px">Shop now</a>
</div>
<div class="abs promo" style="left:599px;top:2394px;background:radial-gradient(circle at 50% 60%,#8a6a58 0%,#3a2a22 60%,#1a1410 100%)" role="img" aria-label="Close-up of sugar-dusted chocolate truffles"></div>
<div class="abs promo" style="left:116px;top:2603px;background:radial-gradient(circle at 44% 40%,#e8e4e8 0%,#5a4a58 12%,#16303a 45%,#0f2228 100%)" role="img" aria-label="Sparkler glowing against a dark night"></div>
<div class="abs promo promo-text" style="left:599px;top:2603px">
  <p style="width:440px">Holidays, birthdays, anniversaries..<br>No matter what you’re celebrating, you’ll find in our handmade chocolates the perfect gift for any occasion.</p>
  <a class="abs btn btn-dark" style="left:250px;top:141px;width:207px;height:50px">Shop now</a>
</div>

<h3 class="abs testi-title serif">Testimonials</h3>
<svg class="abs" style="left:116px;top:2964px" width="32" height="32" viewBox="0 0 32 32"><circle cx="16" cy="16" r="16" fill="#000"/><path d="M19 9l-7 7 7 7" fill="none" stroke="#fff" stroke-width="3"/></svg>
<svg class="abs" style="left:1051px;top:2964px" width="32" height="32" viewBox="0 0 32 32"><circle cx="16" cy="16" r="16" fill="#000"/><path d="M13 9l7 7-7 7" fill="none" stroke="#fff" stroke-width="3"/></svg>
<p class="abs testi-copy">Our clients loved their hand-crafted chocolates. Thanks so much for putting in the time and effort (and love) to make something so delicious and for the added touch of hand-wrapping the bows on the boxes and making sure our brand (and our good taste in chocolates) stands out for all the right reasons.</p>
<div class="abs stars">★★★★★</div>
<div class="abs testi-rule"></div>
<div class="abs testi-name serif">Leon Hartley</div>
<div class="abs testi-role serif">Director, Northgate Media</div>

<footer class="abs site-footer">
  <h4 class="abs footer-head" style="left:118px;top:40px">CONTACT US</h4>
  <ul class="abs footer-list" style="left:117px;top:90px">
    <li>74 Harwood Rd</li><li>Kingsgrove</li><li>NSW, Australia</li><li>Tel: +61 2 9000 4417</li><li>Email: hello@marlowconfections.com.au</li>
  </ul>
  <h4 class="abs footer-head" style="left:445px;top:40px">QUICK LINKS</h4>
  <ul class="abs footer-list" style="left:446px;top:90px">
    <li>Recipes</li><li>Terms and Conditions</li><li>Privacy Policy</li><li>Shipping Policy</li><li>Sitemap</li>
  </ul>
  <h4 class="abs footer-head" style="left:691px;top:40px">OUR NEWSLETTER</h4>
  <div class="abs newsletter-input">Your Email</div>
  <a class="abs btn newsletter-btn">Subscribe</a>
  <h4 class="abs footer-head" style="left:691px;top:180px">STAY IN TOUCH</h4>
  <div class="abs social" aria-label="Social links"><span></span><span></span><span></span><span></span><span></span></div>
  <a class="abs btn btn-light map-btn">Look for us on the map</a>
  <div class="abs footer-rule"></div>
  <div class="abs copyright">© 2020 Marlow Confections. All Rights Reserved.</div>
</footer>

</body>
</html>
```